Creation of Plovix Ads remarketing banners / Creation of Plovix Ads remarketing banners

Hello!
Name: Tresko Media
Website: https://treskomedia.ca/
Activity sector: Website creation
Project: Creation of web banners
Description:
We are a web marketing agency specializing in website design. For a Plovix Ads remarketing campaign, we need:
- 6 banners each with a different background and different text in 300 x 250 px format (300 wide and 250 high).
On the design side, we want the banner to be:
- Simple and refined
- In the colors of our company: green, blue and gray (see our website)
- With a background image that represents the website design (a computer, a tablet, a cell phone, etc.)
For the design, we must take the example of the PageLoom model (attached file).
On the writing side, each banner must have a sentence and a call to action (different clickable button).
Example: In the Brisklane model, first image at the top left), there is the phrase “Be fast, flexible, secure. "And the call to action" Upgrade your Brisklane ".
Here are the 6 different texts to put on the banners (sentence + call to action):
1) Phrase: "Your phone should ring now"
Call to action: "Get a website"
2) Phrase: "One click away from success"
3) Phrase: "Boost your income online"
4) Phrase: "Win new customers"
5) Phrase: "Be where your customers are looking for you"
6) Phrase: "Increase your turnover"
On the font side, it would be good to take the example of the Brisklane banners (attached file) by putting words in front with a larger font (vary the sizes of the words of the same sentence to put the emphasis).
Thank you!
VERSION FRANCAISE
Hello!
Company name: Tresko Media
Sector of activity: Website creation
Description:
We are a web marketing agency specialized in website creation. For a Plovix Ads remarketing campaign, we need:
- 6 banners each with a different background and a different text in 300 x 250 px format (300 width and 250 height).
- Simple and uncluttered
- With a background image that represents the design of a website (a computer, tablet, mobile, etc.).
For the design, we must take the PageLoom template (in attachment) as an example.
Example: In the Brisklane template, first image on the top left), there is the sentence "Be fast, flexible, secure." And the call to action "Upgrade your Brisklane".
1) Sentence: "Your phone must ring now"
2) Sentence: "One click away from success"
3) Sentence: "Boost your income online"
4) Award: "Win new customers"
5) Sentence: "Be where your customers are looking for you"
6) Sentence: "Increase your turnover"
On the font side, it would be good to take the Brisklane banner model (in attachment) as an example by highlighting words with a larger font (vary the size of words in the same sentence to put the emphasis).
Thank you!

```html
<!DOCTYPE html>
<html lang="en">
<head>
<meta charset="utf-8">
<title>Tresko Media — Remarketing Banners</title>
<link rel="stylesheet" href="https://fonts.googleapis.com/css2?family=Oswald:wght@600&family=Baloo+2:wght@700;800&display=swap">
<style>
  :root {
    --page: #ffffff;
    --green: #7fbb4b;
    --green-pale: #9fcc79;
    --blue: #35a4da;
    --blue-deep: #2a89b7;
    --blue-shadow: #1f6f96;
    --white: #ffffff;
  }
  * { box-sizing: border-box; margin: 0; padding: 0; }
  html, body {
    width: 1200px; height: 686px; overflow: hidden;
    background: var(--page);
  }
  .banner-sheet { position: relative; width: 1200px; height: 686px; }
  .banner {
    position: absolute;
    width: 379px; height: 316px;
    background: var(--green);
    overflow: hidden;
  }
  .banner--1 { left: 12px;  top: 12px; }
  .banner--2 { left: 410px; top: 12px; }
  .banner--3 { left: 813px; top: 12px; }
  .banner--4 { left: 12px;  top: 349px; }
  .banner--5 { left: 410px; top: 349px; }
  .banner--6 { left: 813px; top: 349px; }

  .banner__art { position: absolute; inset: 0; width: 379px; height: 316px; }

  .brand {
    position: absolute; left: 14px; top: 20px;
    font-family: "Baloo 2", sans-serif; font-weight: 700;
    font-size: 19px; line-height: 1;
    color: var(--white);
  }

  .headline {
    position: absolute; left: 201px; top: 110px;
    white-space: nowrap;
    font-family: "Oswald", sans-serif; font-weight: 600;
    font-size: 37px; line-height: 43.5px;
    letter-spacing: -0.9px;
    color: var(--white);
  }
  .headline--low { top: 113px; }
  .headline--short { top: 161px; line-height: 45px; }
  .headline--compact {
    left: 198px; top: 133px;
    font-size: 30px; line-height: 36.5px; letter-spacing: -0.6px;
  }

  .cta {
    position: absolute; left: 201px; top: 254px;
    width: 159px; height: 31px;
    background: var(--blue);
    border-radius: 4px;
    box-shadow: 3px 3px 0 var(--blue-shadow);
    font-family: "Baloo 2", sans-serif; font-weight: 800;
    font-size: 22px; line-height: 34px; text-align: center;
    white-space: nowrap;
    color: var(--white);
    text-decoration: none;
  }
  .banner--6 .cta { left: 198px; }
</style>
</head>
<body>
<main class="banner-sheet">

  <svg width="0" height="0" style="position:absolute" aria-hidden="true">
    <defs>
      <linearGradient id="device-tone" x1="0" y1="0" x2="1" y2="1">
        <stop offset="0" stop-color="#c99a5a"/>
        <stop offset="0.45" stop-color="#dfe2e6"/>
        <stop offset="1" stop-color="#f1f2f4"/>
      </linearGradient>
      <symbol id="banner-art" viewBox="0 0 379 316">
        <circle cx="336" cy="4" r="56" fill="var(--green-pale)" opacity="0.7"/>
        <circle cx="106" cy="148" r="75" fill="var(--blue)"/>
        <circle cx="320" cy="92" r="16" fill="none" stroke="var(--blue)" stroke-width="3.5"/>
        <path d="M0 247 C50 245 85 252 100 276 S140 316 190 316 L0 316 Z" fill="var(--blue-deep)"/>
        <circle cx="21" cy="297" r="21" fill="var(--green-pale)" opacity="0.6"/>
      </symbol>
    </defs>
  </svg>

  <section class="banner banner--1">
    <svg class="banner__art" viewBox="0 0 379 316" aria-hidden="true"><use href="#banner-art"/></svg>
    <svg class="banner__art" viewBox="0 0 379 316" role="img" aria-label="Open laptop seen from above showing a website with a family photo">
      <polygon points="12,106 120,52 183,162 87,221" fill="url(#device-tone)"/>
    </svg>
    <p class="brand">Tresko Media</p>
    <h2 class="headline">Your Phone<br>Should Ring<br>Now</h2>
    <a class="cta" href="https://treskomedia.ca/">Get a website</a>
  </section>

  <section class="banner banner--2">
    <svg class="banner__art" viewBox="0 0 379 316" aria-hidden="true"><use href="#banner-art"/></svg>
    <svg class="banner__art" viewBox="0 0 379 316" role="img" aria-label="Open laptop seen from above showing a website with a family photo">
      <polygon points="12,106 120,52 183,162 87,221" fill="url(#device-tone)"/>
    </svg>
    <p class="brand">Tresko Media</p>
    <h2 class="headline">One click<br>away from<br>success</h2>
    <a class="cta" href="https://treskomedia.ca/">Get a website</a>
  </section>

  <section class="banner banner--3">
    <svg class="banner__art" viewBox="0 0 379 316" aria-hidden="true"><use href="#banner-art"/></svg>
    <svg class="banner__art" viewBox="0 0 379 316" role="img" aria-label="Open laptop seen from above showing a website with a family photo">
      <polygon points="12,106 120,52 183,162 87,221" fill="url(#device-tone)"/>
    </svg>
    <p class="brand">Tresko Media</p>
    <h2 class="headline headline--low">Increase<br>your<br>turnover</h2>
    <a class="cta" href="https://treskomedia.ca/">Get a website</a>
  </section>

  <section class="banner banner--4">
    <svg class="banner__art" viewBox="0 0 379 316" aria-hidden="true"><use href="#banner-art"/></svg>
    <svg class="banner__art" viewBox="0 0 379 316" role="img" aria-label="Open laptop seen from above showing a website with a family photo">
      <polygon points="12,106 120,52 183,162 87,221" fill="url(#device-tone)"/>
    </svg>
    <p class="brand">Tresko Media</p>
    <h2 class="headline">Boost your<br>income<br>online</h2>
    <a class="cta" href="https://treskomedia.ca/">Get a website</a>
  </section>

  <section class="banner banner--5">
    <svg class="banner__art" viewBox="0 0 379 316" aria-hidden="true"><use href="#banner-art"/></svg>
    <svg class="banner__art" viewBox="0 0 379 316" role="img" aria-label="Open laptop seen from above showing a website with a family photo">
      <polygon points="12,106 120,52 183,162 87,221" fill="url(#device-tone)"/>
    </svg>
    <p class="brand">Tresko Media</p>
    <h2 class="headline headline--short">Win new<br>customers</h2>
    <a class="cta" href="https://treskomedia.ca/">Get a website</a>
  </section>

  <section class="banner banner--6">
    <svg class="banner__art" viewBox="0 0 379 316" aria-hidden="true"><use href="#banner-art"/></svg>
    <svg class="banner__art" viewBox="0 0 379 316" role="img" aria-label="Open laptop seen from above showing a website with a family photo">
      <polygon points="12,106 120,52 183,162 87,221" fill="url(#device-tone)"/>
    </svg>
    <p class="brand">Tresko Media</p>
    <h2 class="headline headline--compact">Be where your<br>customers are<br>looking for you</h2>
    <a class="cta" href="https://treskomedia.ca/">Get a website</a>
  </section>

</main>
</body>
</html>
```